The Ledgerline Business Card

Business card with QR Code for an accounting and tax business

Target Market(s)

Small Business and Individual Tax

Industry/Entity Type

Bookkeeping, Accounting and Taxes

Contact Information for Business Card

482 CALDWELL ST STE 2210 #614273 BOSTON, MA Zip: 02387

Requirements
Must have
• Name and Address

```html
<!DOCTYPE html>
<html lang="en">
<head>
<meta charset="utf-8">
<title>The Ledgerline Business Card</title>
<link rel="stylesheet" href="https://fonts.googleapis.com/css2?family=Playfair+Display:wght@400;700&display=swap">
<style>
  :root {
    --stage: #2b2e33;
    --card-light: #ffffff;
    --card-dark: #262626;
    --ink: #1c1c1c;
    --ink-soft: #4a4a4a;
    --emboss: #3a3a3a;
  }
  * { margin: 0; padding: 0; box-sizing: border-box; }
  html, body {
    width: 1200px;
    height: 952px;
    overflow: hidden;
    background: var(--stage);
    font-family: "Playfair Display", Georgia, serif;
  }
  .canvas {
    position: relative;
    width: 1200px;
    height: 952px;
  }
  .card {
    position: absolute;
    border-radius: 3px;
    box-shadow: 0 14px 30px rgba(0,0,0,0.45);
  }
  .card-front {
    left: 600px;
    top: 140px;
    width: 530px;
    height: 303px;
    background: var(--card-light);
    color: var(--ink);
  }
  .card-back {
    left: 170px;
    top: 330px;
    width: 303px;
    height: 530px;
    background: var(--card-dark);
  }
  .brand {
    position: absolute;
    display: flex;
    align-items: center;
    gap: 10px;
    font-weight: 400;
    white-space: nowrap;
  }
  .brand-dot {
    display: block;
    border-radius: 50%;
    border: 2px solid currentColor;
  }
  .card-front .brand {
    left: 34px;
    top: 62px;
    font-size: 21px;
    color: var(--ink);
  }
  .card-front .brand-dot { width: 26px; height: 26px; }
  .identity {
    position: absolute;
    left: 214px;
    top: 118px;
    right: 0;
  }
  .person-name {
    font-weight: 700;
    font-size: 27px;
    letter-spacing: 1px;
    padding-bottom: 6px;
    border-bottom: 2px solid var(--ink);
  }
  .person-role {
    margin-top: 6px;
    font-size: 13px;
    color: var(--ink-soft);
  }
  .address {
    margin-top: 8px;
    font-size: 14px;
    line-height: 1.4;
    color: var(--ink-soft);
    font-style: normal;
  }
  .card-back .brand {
    left: 0;
    right: 0;
    top: 150px;
    justify-content: center;
    font-size: 22px;
    color: var(--emboss);
  }
  .card-back .brand-dot { width: 26px; height: 26px; }
</style>
</head>
<body>
  <main class="canvas">
    <section class="card card-back" aria-label="Card back">
      <div class="brand">
        <span class="brand-dot"></span>
        <span class="brand-name">The Ledgerline</span>
      </div>
    </section>

    <section class="card card-front" aria-label="Card front">
      <div class="brand">
        <span class="brand-dot"></span>
        <span class="brand-name">The Ledgerline</span>
      </div>
      <div class="identity">
        <h1 class="person-name">DARA WHITFIELD</h1>
        <p class="person-role">Managing Director</p>
        <address class="address">
          482 Caldwell St Ste 2210 #614273<br>
          Boston, Ma Zip: 02387
        </address>
      </div>
    </section>
  </main>
</body>
</html>
```